Brightmere Business Card Redesign & Logo Update

We need to update our business cards to something more modern and fresh. Brightmere can provide the current color schemes and old design examples, but welcome creativity in helping us with this redesign. PLEASE NOTE that we no longer utilize the "tree" and/or "leaf" imagery in our branding. If able would apprecaite an update on the quality of our "words only" logo in Ai. / PNG formats too.

Target Market(s)

Investors, landowners, corporate partners, contractors

Industry/Entity Type

Environmental Restoration & Conservation

Contact Information for Business Card

Logo, persons name, title, mailing address, phone and email, website url

Font styles to use
Other font styles liked:
• Merriweather

Requirements
Nice to have
• Logo, persons name, title, mailing address, phone and email, website url, but open to ideams
Should not have
• No all back backgrounds

```html
<!DOCTYPE html>
<html lang="en">
<head>
<meta charset="utf-8">
<title>Brightmere Business Card</title>
<link rel="stylesheet" href="https://fonts.googleapis.com/css2?family=Oswald:wght@500;600&family=Roboto:wght@400&display=swap">
<style>
  :root {
    --backdrop: #4b4b4b;
    --card-light: #ffffff;
    --card-deep: #10301f;
    --orange: #ee7b05;
    --green: #137b36;
    --ink: #1c1c1c;
    --muted: #3a3a3a;
    --rule: #b5b5b5;
  }
  * { margin: 0; padding: 0; box-sizing: border-box; }
  html, body {
    width: 1093px; height: 1200px; overflow: hidden;
    background: var(--backdrop);
  }
  .canvas { position: relative; width: 1093px; height: 1200px; }

  .card {
    position: absolute;
    border-radius: 28px;
    overflow: hidden;
    box-shadow: 2px 4px 6px rgba(0,0,0,0.55);
  }
  .card--front { left: 265px; top: 226px; width: 577px; height: 356px; background: var(--card-light); }
  .card--back  { left: 265px; top: 621px; width: 583px; height: 356px; background: var(--card-deep); }

  .accent-band { position: absolute; left: 0; right: 0; bottom: 0; height: 19px; display: flex; }
  .accent-band__orange { flex: 0 0 290px; background: var(--orange); }
  .accent-band__green { flex: 1; background: var(--green); }

  .wordmark {
    position: absolute;
    font-family: "Oswald", "Arial Narrow", sans-serif;
    font-weight: 600;
    color: var(--orange);
    text-transform: uppercase;
    line-height: 1;
    white-space: nowrap;
  }
  .card--front .wordmark { left: 40px; width: 226px; top: 143px; font-size: 41px; letter-spacing: 0; text-align: center; }
  .card--back .wordmark { left: 0; right: 0; top: 124px; text-align: center; font-size: 59px; letter-spacing: 0.5px; }

  .divider { position: absolute; left: 289px; top: 75px; width: 1px; height: 208px; background: var(--rule); }

  .details { position: absolute; left: 311px; top: 86px; font-family: "Roboto", Arial, sans-serif; color: var(--ink); }
  .person__name {
    font-family: "Oswald", "Arial Narrow", sans-serif;
    font-weight: 500; font-size: 29px; line-height: 1; text-transform: uppercase;
    letter-spacing: -0.3px;
  }
  .person__first { color: var(--orange); }
  .person__last { color: var(--green); }
  .person__title { font-size: 16px; color: var(--muted); line-height: 1.1; margin-top: 1px; }

  .contact-list { list-style: none; margin-top: 16px; }
  .contact-list li { display: flex; align-items: center; font-size: 16.5px; line-height: 21px; }
  .contact-list svg { width: 15px; height: 15px; margin-right: 7px; flex: none; }
  .highlight { color: var(--orange); }

  .address { margin-top: 11px; font-size: 16.5px; line-height: 21px; }
</style>
</head>
<body>
<div class="canvas">

  <section class="card card--front">
    <div class="wordmark">Brightmere</div>
    <div class="divider"></div>
    <div class="details">
      <div class="person__name"><span class="person__first">Daniel</span> <span class="person__last">Hartley</span></div>
      <div class="person__title">Managing Director</div>
      <ul class="contact-list">
        <li>
          <svg viewBox="0 0 16 16" aria-hidden="true"><path d="M4 1.5l2.3 3-1.4 1.6c.8 1.9 2.4 3.5 4.3 4.3l1.6-1.4 3 2.3-1.3 2.4C7 13.7 2.3 9 1.6 3z" fill="none" stroke="var(--orange)" stroke-width="1.5" stroke-linejoin="round"/><path d="M10 2.5a4 4 0 0 1 3.5 3.5M10 5a1.6 1.6 0 0 1 1 1" fill="none" stroke="var(--orange)" stroke-width="1.3" stroke-linecap="round"/></svg>
          044-123 456 789
        </li>
        <li>
          <svg viewBox="0 0 16 16" aria-hidden="true"><rect x="0.5" y="3" width="15" height="10" fill="var(--orange)"/><path d="M0.5 3.5l7.5 6 7.5-6M0.5 13l5.5-5M15.5 13l-5.5-5" fill="none" stroke="#fff" stroke-width="1"/></svg>
          info@webname.com
        </li>
        <li>
          <svg viewBox="0 0 16 16" aria-hidden="true"><g fill="none" stroke="var(--orange)" stroke-width="1.3"><circle cx="8" cy="8" r="6.8"/><ellipse cx="8" cy="8" rx="3" ry="6.8"/><path d="M1.2 8h13.6M2.3 4.5h11.4M2.3 11.5h11.4"/></g></svg>
          www.<span class="highlight">websitename</span>.com
        </li>
      </ul>
      <p class="address">421, Address line goes here<br>45452,Country Name</p>
    </div>
    <div class="accent-band"><span class="accent-band__orange"></span><span class="accent-band__green"></span></div>
  </section>

  <section class="card card--back">
    <div class="wordmark">Brightmere</div>
    <div class="accent-band"><span class="accent-band__orange"></span><span class="accent-band__green"></span></div>
  </section>

</div>
</body>
</html>
```